Dumpling Packaging - Modern/Contemporary and Unique

We need five designs for frozen dumplings and pierogies ( this dumplings/pierogies are Russian/Ukrainian/Belorussian, not to be confused with the Chinese ones as they have very different form and filling and obviously the packaging style is very different) . The product will be sold in USA. The design should be modern, unique, and catch the eye of the consumer. The color for the packaging and main things like logos and small nuances will remain the same on all of them. We want the color of the packaging to be on the darker side. It can be one toned or couple of tones transitioning one into another ( look at examples of packages that are attached). The front of the packaging should have the logo on the top, on the bottom the weight as on the packaging size attachment( it will be the same on all of them), keep frozen sign, and US inspected logo. Under our logo on the top there should be slogan- Best of the Best. Under the slogan there should be the name of the product - Beef Dumplings, Pork Dumplings, Beef and Pork Dumplings, Chicken Dumplings, Potato Pierogies with Bacon. In the left corner there should be a see through window left so that the customer can see the product inside. The size of the opening will depend on the main part that you will use. The main part on the front of the label is that we want a picture of raw meat that the dumplings contain (no ground meats). But it shouldn't be just a picture or drawing, we want it to be made using AI. I've attached three pictures of meat but they are not the one you are to use but just as an example. You can use bigger cuts of meat as long as you can see good quality meat and it looks appealing. Plus some of packages that are attached also have raw meat on the front. So that it looks real but looks better then just real meat. For Beef dumplings the meat should be beef, for chicken dumplings use chicken meat ( you can use both red and white chicken meat), for pork use pork, for beef and pork use beef and pork, for pierogies use potato, bacon, and onion, maybe spices. Don't use meat on bones. No picture of alive animals should be present on the packaging. At the back you need to put nutritional facts and ingredients on one side( they are all attached) and type MANUFACTURED FOR: PANTRY ORBIT 40218 NE 7th CT, Davie, Fl 33325. Also place a small Made in USA logo somewhere in the corner. On the other half of the back you need to put again the name of the dumpling, under cooking instructions ( attached as a word file), under put Safe Handling Instructions, and under place a barcode for specific product ( all five barcodes are attached). I have attached 8 pictures of different dumplings packages that I think slightly resonate with our idea- they have dark colored background, look modern, some have a see through opening of the product. I attached the packaging size as it will go in the print so please follow the sizing standard.

```html
<!DOCTYPE html>
<html lang="en">
<head>
<meta charset="utf-8">
<title>Pantry Orbit Steamed Dumplings – Packaging Range</title>
<link rel="stylesheet" href="https://fonts.googleapis.com/css2?family=Bebas+Neue&family=Kaushan+Script&display=swap">
<style>
  :root {
    --canvas: #ffffff;
    --pack-body: #2b2b2d;
    --pack-band: #050505;
    --window: #8b8b8f;
    --text-light: #f2f2f2;
    --rule: #bdbdbd;
    --gold: #c9a67a;
    --chicken: #c77d43;
    --beef: #b8383b;
    --pork: #2c88b6;
  }
  * { box-sizing: border-box; margin: 0; padding: 0; }
  html, body { width: 1200px; height: 763px; overflow: hidden; background: var(--canvas); }
  .range { position: relative; width: 1200px; height: 763px; }

  .pack {
    position: absolute;
    width: 380px; height: 543px;
    background: var(--pack-body);
    overflow: hidden;
    font-family: "Bebas Neue", sans-serif;
    font-weight: 400;
    color: var(--text-light);
    transform-origin: 0 0;
  }
  .pack--chicken { left: 54px; top: 92px; --accent: var(--chicken); }
  .pack--pork { left: 762px; top: 92px; --accent: var(--pork); }
  .pack--beef { left: 399px; top: 138px; --accent: var(--beef); transform: scale(1.05); z-index: 2; box-shadow: 0 0 14px rgba(0,0,0,.35); }

  .pack__band { position: absolute; left: 0; top: 0; width: 100%; height: 46px; background: var(--pack-band); }
  .pack__photo { position: absolute; left: 0; top: 200px; width: 380px; height: 343px; }
  .pack--chicken .pack__photo { background: radial-gradient(ellipse at 62% 58%, #e3b3a2 0%, #b88a7a 24%, #4a3f3a 55%, #262627 85%); }
  .pack--beef .pack__photo { background: radial-gradient(ellipse at 58% 62%, #b5454a 0%, #8a3034 26%, #40302f 58%, #262627 88%); }
  .pack--pork .pack__photo { background: radial-gradient(ellipse at 62% 60%, #d9959a 0%, #b07375 25%, #463a38 56%, #262627 86%); }
  .pack__photo::before {
    content: ""; position: absolute; inset: 0;
    background: linear-gradient(to bottom, var(--pack-body) 0%, rgba(43,43,45,0) 30%, rgba(20,20,20,0) 85%, rgba(15,15,15,.6) 100%);
  }

  .pack__tab {
    position: absolute; left: 48px; top: 0; width: 178px; height: 162px;
    background: var(--accent);
    display: flex; align-items: center; justify-content: center;
    padding-top: 44px;
  }
  .pack__tab-lines { position: absolute; left: 0; top: 0; width: 100%; height: 44px; }
  .brand-name { font-size: 28px; letter-spacing: 1px; color: #ffffff; line-height: 1; }

  .pack__window { position: absolute; left: 241px; top: 60px; width: 100px; height: 102px; border-radius: 12px; background: var(--window); }

  .product-title { position: absolute; left: 50px; top: 186px; width: 186px; line-height: .9; font-weight: 400; }
  .product-title__meat { font-size: 44px; display: inline-block; vertical-align: bottom; }
  .product-title__style {
    display: inline-block; vertical-align: bottom; margin-left: 5px; margin-bottom: 5px;
    font-size: 19px; line-height: 1; padding: 2px 0 1px; letter-spacing: .5px;
    border-top: 1px solid var(--rule); border-bottom: 1px solid var(--rule);
  }
  .product-title__kind { display: block; font-size: 48px; margin-top: 3px; }
  .product-title__tagline { display: block; font-family: "Kaushan Script", cursive; font-size: 20px; line-height: 1.2; color: var(--gold); margin: 4px 0 0 12px; }

  .claims { position: absolute; left: 244px; top: 188px; list-style: none; font-size: 15px; line-height: 22px; white-space: nowrap; }
  .claims li { display: flex; align-items: center; gap: 5px; }
  .claims svg { width: 9px; height: 11px; flex: none; }

  .pack__info { position: absolute; left: 50px; top: 464px; font-size: 15px; line-height: 19px; letter-spacing: .3px; }
</style>
</head>
<body>
<main class="range">

  <section class="pack pack--chicken">
    <div class="pack__photo" role="img" aria-label="Photo of raw chicken pieces in a dark bowl with rosemary, garlic, spices and pierogi-style dumplings"></div>
    <div class="pack__band"></div>
    <div class="pack__tab">
      <svg class="pack__tab-lines" viewBox="0 0 178 44" preserveAspectRatio="none"><g stroke="rgba(0,0,0,.25)" stroke-width="1"><line x1="0" y1="6" x2="178" y2="6"/><line x1="0" y1="13" x2="178" y2="13"/><line x1="0" y1="20" x2="178" y2="20"/><line x1="0" y1="27" x2="178" y2="27"/><line x1="0" y1="34" x2="178" y2="34"/><line x1="0" y1="41" x2="178" y2="41"/></g></svg>
      <span class="brand-name">PANTRY ORBIT</span>
    </div>
    <div class="pack__window"></div>
    <h2 class="product-title"><span class="product-title__meat">CHICKEN</span><span class="product-title__style">STEAMED</span><span class="product-title__kind">DUMPLINGS</span><span class="product-title__tagline">Original recipe</span></h2>
    <ul class="claims">
      <li><svg viewBox="0 0 10 12"><path d="M1 7 L4 11 L9 1" fill="none" stroke="var(--accent)" stroke-width="1.4"/></svg>100% ORGANIC</li>
      <li><svg viewBox="0 0 10 12"><path d="M1 7 L4 11 L9 1" fill="none" stroke="var(--accent)" stroke-width="1.4"/></svg>NON PRESERVATIVES</li>
      <li><svg viewBox="0 0 10 12"><path d="M1 7 L4 11 L9 1" fill="none" stroke="var(--accent)" stroke-width="1.4"/></svg>NON GMO</li>
    </ul>
    <p class="pack__info">KEEP FROZEN<br>NET WT. 2oz (800GR)</p>
  </section>

  <section class="pack pack--pork">
    <div class="pack__photo" role="img" aria-label="Photo of raw pork steaks on a wooden board with peppercorns, garlic, rosemary, salt and dumplings in a bowl"></div>
    <div class="pack__band"></div>
    <div class="pack__tab">
      <svg class="pack__tab-lines" viewBox="0 0 178 44" preserveAspectRatio="none"><g stroke="rgba(0,0,0,.25)" stroke-width="1"><line x1="0" y1="6" x2="178" y2="6"/><line x1="0" y1="13" x2="178" y2="13"/><line x1="0" y1="20" x2="178" y2="20"/><line x1="0" y1="27" x2="178" y2="27"/><line x1="0" y1="34" x2="178" y2="34"/><line x1="0" y1="41" x2="178" y2="41"/></g></svg>
      <span class="brand-name">PANTRY ORBIT</span>
    </div>
    <div class="pack__window"></div>
    <h2 class="product-title"><span class="product-title__meat">PORK</span><span class="product-title__style">STEAMED</span><span class="product-title__kind">DUMPLINGS</span><span class="product-title__tagline">Original recipe</span></h2>
    <ul class="claims">
      <li><svg viewBox="0 0 10 12"><path d="M1 7 L4 11 L9 1" fill="none" stroke="var(--accent)" stroke-width="1.4"/></svg>100% ORGANIC</li>
      <li><svg viewBox="0 0 10 12"><path d="M1 7 L4 11 L9 1" fill="none" stroke="var(--accent)" stroke-width="1.4"/></svg>NON PRESERVATIVES</li>
      <li><svg viewBox="0 0 10 12"><path d="M1 7 L4 11 L9 1" fill="none" stroke="var(--accent)" stroke-width="1.4"/></svg>NON GMO</li>
    </ul>
    <p class="pack__info">KEEP FROZEN<br>NET WT. 2oz (800GR)</p>
  </section>

  <section class="pack pack--beef">
    <div class="pack__photo" role="img" aria-label="Photo of raw beef slices in a dark bowl with rosemary, peppercorns, salt and a bowl of dumplings"></div>
    <div class="pack__band"></div>
    <div class="pack__tab">
      <svg class="pack__tab-lines" viewBox="0 0 178 44" preserveAspectRatio="none"><g stroke="rgba(0,0,0,.25)" stroke-width="1"><line x1="0" y1="6" x2="178" y2="6"/><line x1="0" y1="13" x2="178" y2="13"/><line x1="0" y1="20" x2="178" y2="20"/><line x1="0" y1="27" x2="178" y2="27"/><line x1="0" y1="34" x2="178" y2="34"/><line x1="0" y1="41" x2="178" y2="41"/></g></svg>
      <span class="brand-name">PANTRY ORBIT</span>
    </div>
    <div class="pack__window"></div>
    <h2 class="product-title"><span class="product-title__meat">BEEF</span><span class="product-title__style">STEAMED</span><span class="product-title__kind">DUMPLINGS</span><span class="product-title__tagline">Original recipe</span></h2>
    <ul class="claims">
      <li><svg viewBox="0 0 10 12"><path d="M1 7 L4 11 L9 1" fill="none" stroke="var(--accent)" stroke-width="1.4"/></svg>100% ORGANIC</li>
      <li><svg viewBox="0 0 10 12"><path d="M1 7 L4 11 L9 1" fill="none" stroke="var(--accent)" stroke-width="1.4"/></svg>NON PRESERVATIVES</li>
      <li><svg viewBox="0 0 10 12"><path d="M1 7 L4 11 L9 1" fill="none" stroke="var(--accent)" stroke-width="1.4"/></svg>NON GMO</li>
    </ul>
    <p class="pack__info">KEEP FROZEN<br>NET WT. 2oz (800GR)</p>
  </section>

</main>
</body>
</html>
```